Lorne Hollow Farm Postcard Design

I am looking for a new postcard design to mail out this season. We are a Farm business that does wholesale and retail and bulk seasoned firewood sales. we sell firewood from anything from bagged wood to tractor trailer loads of wood. We sell firewood in bulk bags. Pick up or delivery available there is no order to big or too small. I need my business name and phone number on the cards Lorne Hollow Farm 848-316-0572 (call or text) I would like it to say we are the best priced guaranteed. I want something that is simple and straight forward but also really catches the eye when they see these in the mail box. I attached my logo and feel free to use photos of split firewood if you would like. id like my email on the card Lornehollowfarm90@mailvista.net.

Target Market(s)

Firewood purchasers

Industry/Entity Type

agriculture

Requirements
Must have
• email phone number logo

```html
<!DOCTYPE html>
<html lang="en">
<head>
<meta charset="utf-8">
<title>Lorne Hollow Farm – Firewood Postcard</title>
<link rel="stylesheet" href="https://fonts.googleapis.com/css2?family=Anton&family=Oswald:wght@500;600&display=swap">
<style>
  :root {
    --ember-dark: #4a1f0e;
    --ember-mid: #8a3a14;
    --flame: #d8741f;
    --wood-light: #e2ad68;
    --wood-mid: #c98a45;
    --wood-dark: #a8692d;
    --rust-band: #8e3417;
    --frame-brown: #6b3414;
    --ink-brown: #5a2a10;
    --paper-white: #ffffff;
    --logo-black: #0d0b0a;
    --logo-orange: #f08a1c;
  }
  * { box-sizing: border-box; margin: 0; padding: 0; }
  html, body { width: 698px; height: 1200px; overflow: hidden; background: #cfcfcf; }
  .postcard {
    position: relative; width: 698px; height: 1200px; overflow: hidden;
    font-family: "Anton", "Oswald", sans-serif;
    background: linear-gradient(170deg, var(--wood-light) 0%, var(--wood-mid) 55%, var(--wood-light) 100%);
  }
  .fire-field {
    position: absolute; left: 0; top: 0; width: 698px; height: 580px;
    background:
      radial-gradient(ellipse 220px 420px at 330px 200px, rgba(232,130,35,.75), transparent 70%),
      radial-gradient(ellipse 160px 300px at 560px 120px, rgba(220,110,30,.55), transparent 70%),
      linear-gradient(160deg, var(--ember-dark) 0%, var(--ember-mid) 45%, var(--ember-dark) 100%);
  }
  .torn-edge { position: absolute; left: 0; top: 540px; width: 698px; height: 50px; z-index: 1; }
  .brand-box {
    position: absolute; left: 27px; top: 2px; width: 203px; height: 194px;
    background: var(--logo-black); border: 2px solid var(--paper-white);
    display: flex; align-items: center; justify-content: center; gap: 10px;
  }
  .brand-mark { width: 14px; height: 14px; background: var(--logo-orange); flex: none; }
  .brand-name {
    font-family: "Anton", sans-serif; color: var(--logo-orange);
    font-size: 30px; line-height: 1.05; text-transform: uppercase;
  }
  .headline {
    position: absolute; left: 23px; top: 200px; width: 470px;
    color: var(--paper-white); font-size: 60px; line-height: 86px;
    font-weight: 400; letter-spacing: -0.5px; z-index: 2;
  }
  .worker-photo {
    position: absolute; left: 500px; top: 122px; width: 198px; height: 436px;
    background: linear-gradient(180deg, #6b4a33 0%, #9a9a8a 55%, #c8e05a 80%, #5a3e2a 100%);
  }
  .photo-frame {
    position: absolute; top: 629px; width: 309px; height: 256px;
    border: 4px solid var(--frame-brown);
  }
  .photo-frame.truck {
    left: 29px;
    background: linear-gradient(180deg, #9cc1d8 0%, #a89888 40%, #7e1e24 65%, #8a8070 100%);
  }
  .photo-frame.woodpile {
    left: 363px;
    background: radial-gradient(circle at 50% 50%, #e8c79a 0%, #c9a06a 60%, #8f6a3e 100%);
  }
  .info-frame { position: absolute; left: 79px; top: 885px; width: 542px; height: 133px; }
  .info-text {
    position: absolute; left: 0; width: 698px; text-align: center;
    font-family: "Oswald", sans-serif; font-weight: 600; color: var(--ink-brown);
    font-size: 27px; line-height: 36px; letter-spacing: -0.6px;
  }
  .info-text.guarantee {
    top: 895px; font-family: "Anton", sans-serif; font-weight: 400;
    color: var(--rust-band); font-size: 30px; letter-spacing: 0;
  }
  .info-text.line-one { top: 938px; }
  .info-text.line-two { top: 980px; }
  .phone-band {
    position: absolute; left: 0; top: 1049px; width: 698px; height: 103px;
    background: var(--rust-band);
    display: flex; align-items: center; justify-content: center;
  }
  .phone-number { color: var(--paper-white); font-size: 60px; letter-spacing: 0.5px; }
  .email {
    position: absolute; left: 0; top: 1160px; width: 698px; text-align: center;
    font-family: "Oswald", sans-serif; font-weight: 600; color: var(--ink-brown);
    font-size: 21px; letter-spacing: -0.4px;
  }
</style>
</head>
<body>
<main class="postcard">
  <div class="fire-field" role="img" aria-label="Close-up of burning firewood logs with flames"></div>

  <div class="worker-photo" role="img" aria-label="Smiling worker in yellow hard hat and safety vest with arms crossed"></div>

  <svg class="torn-edge" viewBox="0 0 698 50" preserveAspectRatio="none" aria-hidden="true">
    <path d="M0 16 L30 10 L55 18 L90 8 L120 15 L160 6 L200 14 L240 9 L280 17 L320 7 L360 13 L400 20 L440 10 L480 16 L520 8 L560 14 L600 18 L640 9 L698 15 L698 50 L0 50 Z" fill="#d79a55"/>
  </svg>

  <div class="brand-box">
    <span class="brand-mark"></span>
    <span class="brand-name">Lorne<br>Hollow<br>Farm</span>
  </div>

  <h1 class="headline">Wholesale, retail,<br>and bulk seasoned<br>firewood sales</h1>

  <div class="photo-frame truck" role="img" aria-label="Red semi tractor truck parked in front of a farm barn"></div>
  <div class="photo-frame woodpile" role="img" aria-label="Stacked split seasoned firewood"></div>

  <svg class="info-frame" viewBox="0 0 542 133" aria-hidden="true">
    <path d="M2 0 V120 H108 M434 120 H540 V0" fill="none" stroke="#6b3414" stroke-width="2"/>
  </svg>
  <p class="info-text guarantee">Best priced, guaranteed</p>
  <p class="info-text line-one">Lorne Hollow Farm, Alder Ridge N.J.</p>
  <p class="info-text line-two">732 555 0184, Bulk firewood</p>

  <div class="phone-band"><span class="phone-number">848-316-0572</span></div>

  <p class="email">Lornehollowfarm90@mailvista.net</p>
</main>
</body>
</html>
```